IT business looking for Standout Letterhead Design

We need a letterhead design for a company based in Marrow Bay, CA called Corvane Systems, Inc. We specialize in IT engineering, installation and technical support pertaining to the department of defense.

We would like to see a design that incorporates the black and gold that matches our company logo.

More information on the company can be found at www.corvane-sys.example

```html
<!DOCTYPE html>
<html lang="en">
<head>
<meta charset="utf-8">
<title>Corvane Systems, Inc. — Letterhead</title>
<link href="https://fonts.googleapis.com/css2?family=Cinzel:wght@400&family=Open+Sans:wght@600&display=swap" rel="stylesheet">
<style>
  :root {
    --ink: #0d0d0d;
    --gold: #f5d400;
    --gold-deep: #e6b800;
    --amber: #f0a500;
    --cream: #fbf6d2;
    --cream-light: #fffdf0;
    --paper: #ffffff;
    --paper-shade: #f1f1f1;
    --text: #1a1a1a;
  }
  html, body {
    margin: 0;
    padding: 0;
    width: 881px;
    height: 1200px;
    overflow: hidden;
    background: var(--paper);
  }
  .letterhead {
    position: relative;
    width: 881px;
    height: 1200px;
    box-sizing: border-box;
    border: 6px solid var(--ink);
    overflow: hidden;
    background: radial-gradient(ellipse at 45% 45%, var(--paper) 0%, var(--paper) 45%, var(--paper-shade) 100%);
  }
  .swooshes {
    position: absolute;
    inset: 0;
    width: 100%;
    height: 100%;
  }
  .brand {
    position: absolute;
    top: 40px;
    left: 20px;
    width: 230px;
    text-align: center;
    font-family: "Cinzel", "Times New Roman", serif;
    font-weight: 400;
    color: var(--ink);
  }
  .brand-mark {
    display: block;
    width: 54px;
    height: 54px;
    margin: 0 auto 14px;
    border-radius: 50%;
    background: var(--gold-deep);
  }
  .brand-name {
    display: block;
    font-size: 40px;
    line-height: 1;
    letter-spacing: 1px;
  }
  .brand-suffix {
    display: block;
    margin-top: 6px;
    font-size: 12px;
    letter-spacing: 1px;
  }
  .contact {
    position: absolute;
    left: 38px;
    bottom: 26px;
    margin: 0;
    padding: 0;
    list-style: none;
    font-family: "Open Sans", Arial, sans-serif;
    font-weight: 600;
    font-size: 15px;
    color: var(--text);
  }
  .contact li {
    display: flex;
    align-items: center;
    height: 28px;
  }
  .contact svg {
    width: 16px;
    height: 16px;
    margin-right: 16px;
    fill: var(--ink);
    flex: none;
  }
</style>
</head>
<body>
<div class="letterhead">
  <svg class="swooshes" viewBox="0 0 869 1188" preserveAspectRatio="none" aria-hidden="true">
    <defs>
      <linearGradient id="header-wash" x1="0" y1="0" x2="1" y2="1">
        <stop offset="0" stop-color="var(--cream)"/>
        <stop offset="1" stop-color="var(--cream-light)"/>
      </linearGradient>
      <linearGradient id="footer-wash" x1="0" y1="0" x2="1" y2="0">
        <stop offset="0" stop-color="var(--cream-light)"/>
        <stop offset="0.6" stop-color="var(--cream)"/>
        <stop offset="1" stop-color="var(--gold)"/>
      </linearGradient>
      <linearGradient id="gold-band" x1="0" y1="0" x2="1" y2="0">
        <stop offset="0" stop-color="var(--gold)"/>
        <stop offset="1" stop-color="var(--gold-deep)"/>
      </linearGradient>
    </defs>

    <path class="header-wash" d="M0,0 H760 C560,110 300,250 0,290 Z" fill="url(#header-wash)"/>
    <path class="header-gold" d="M0,195 C260,215 520,120 720,0 H790 C560,120 300,250 0,262 Z" fill="url(#gold-band)"/>
    <path class="header-black" d="M0,282 C300,258 590,110 869,8 V34 C600,150 310,318 0,342 Z" fill="var(--ink)"/>
    <path class="header-line" d="M420,50 C600,20 760,12 869,40 V46 C760,22 600,30 420,56 Z" fill="var(--ink)" opacity="0.85"/>

    <path class="footer-wash" d="M0,950 C260,985 520,1130 869,1140 V1188 H0 Z" fill="url(#footer-wash)"/>
    <path class="footer-amber" d="M0,1002 C120,1004 220,1010 330,1030 L330,1034 C220,1016 120,1010 0,1008 Z" fill="var(--amber)"/>
    <path class="footer-black" d="M0,900 C260,930 520,1090 869,1108 V1142 C520,1138 260,990 0,955 Z" fill="var(--ink)"/>
    <path class="footer-gold" d="M420,1150 C600,1172 760,1160 869,1150 V1178 C760,1184 600,1186 420,1160 Z" fill="url(#gold-band)"/>
    <path class="footer-line" d="M300,1160 C520,1196 720,1176 869,1168 V1172 C720,1182 520,1200 300,1164 Z" fill="var(--ink)"/>
  </svg>

  <div class="brand">
    <span class="brand-mark"></span>
    <span class="brand-name">CORVANE</span>
    <span class="brand-suffix">SYSTEMS, INC.</span>
  </div>

  <ul class="contact">
    <li>
      <svg viewBox="0 0 16 16" aria-hidden="true"><path d="M8 0a5.5 5.5 0 0 0-5.5 5.5C2.5 9.6 8 16 8 16s5.5-6.4 5.5-10.5A5.5 5.5 0 0 0 8 0zm0 7.8a2.3 2.3 0 1 1 0-4.6 2.3 2.3 0 0 1 0 4.6z"/></svg>
      Marrow Bay, CA
    </li>
    <li>
      <svg viewBox="0 0 16 16" aria-hidden="true"><path d="M3.6 0.8l2.2 2.8c.4.5.3 1.1-.1 1.5L4.4 6.3c.9 2 2.9 4 5.3 5.3l1.2-1.3c.4-.4 1-.5 1.5-.1l2.8 2.2c.5.4.5 1.1.1 1.6l-1.3 1.3C12.4 16.9 0 9.2 0.7 3.4L2 2c.5-.5 1.2-.6 1.6-1.2z"/></svg>
      555-010-0148 / 555-010-0172
    </li>
    <li>
      <svg viewBox="0 0 16 16" aria-hidden="true"><path d="M0 3h16v1.2L8 9 0 4.2z M0 5.8l8 4.8 8-4.8V13H0z"/></svg>
      info@corvane-sys.example
    </li>
    <li>
      <svg viewBox="0 0 16 16" aria-hidden="true"><path d="M8 0a8 8 0 1 0 0 16A8 8 0 0 0 8 0zm5.9 7.2h-2.6a12 12 0 0 0-1-4.9 6.4 6.4 0 0 1 3.6 4.9zM8 1.7c.7 1 1.5 2.9 1.7 5.5H6.3C6.5 4.6 7.3 2.7 8 1.7zM5.7 2.3a12 12 0 0 0-1 4.9H2.1a6.4 6.4 0 0 1 3.6-4.9zM2.1 8.8h2.6a12 12 0 0 0 1 4.9 6.4 6.4 0 0 1-3.6-4.9zM8 14.3c-.7-1-1.5-2.9-1.7-5.5h3.4c-.2 2.6-1 4.5-1.7 5.5zm2.3-.6a12 12 0 0 0 1-4.9h2.6a6.4 6.4 0 0 1-3.6 4.9z"/></svg>
      www.corvane-sys.example
    </li>
  </ul>
</div>
</body>
</html>
```